Kickmark Figures Service

We have a football stats service that we feel would benefit from some design input. In particular we would like the designer to look at three pages. We will then transfer this style across the rest of the site.

We are looking for designs for three pages. Links to the existing pages we would like reworked are:

Player:
http://demostats.kickmark-example.com/Player.asp?lang=&coid=4&teid=220&plid=197404

Team Stats:
http://demostats.kickmark-example.com/Team_Stats.asp?lang=&coid=4&teid=218

League Table:
http://demostats.kickmark-example.com/Comp_Table.asp?lang=&coid=4

We require the page structure to remain as is with the main country/competition selector on the left and the content on the right.

The colour palette, fonts, content separators etc are all in your hands. We will use this version as a sales tool for our services. In many cases this will be restyled to match a specific clients requirements.

We are happy for this to be done in HTML/CSS or as a layered image file.

Target Market(s)

These stats pages are for use on newspaper and bookmaker websites.

Industry/Entity Type

Sales

Requirements
Nice to have
• A nice colour palette for graphs and charts is important.

```html
<!DOCTYPE html>
<html lang="en">
<head>
<meta charset="utf-8">
<title>Player Screen – Kickmark Figures Service</title>
<link href="https://fonts.googleapis.com/css2?family=Open+Sans:wght@400;600;700&display=swap" rel="stylesheet">
<style>
:root{
  --bg-top:#d2cdd2;
  --bg-bottom:#f3ddd0;
  --title:#a8a2a6;
  --bar:#2e323d;
  --side:#4b5566;
  --side-head:#3a414f;
  --side-line:#434c5c;
  --side-text:#d8dce3;
  --orange:#e9592c;
  --blue:#2f7fe0;
  --yellow:#f6c900;
  --profile:#f1f0eb;
  --row-a:#f3f3ef;
  --row-b:#f9f9f7;
  --text:#333640;
  --line:#e2e2e2;
  --chart-blue:#3166cf;
  --chart-red:#f0132f;
  --pitch-light:#eef2ea;
  --pitch-mid:#c9d7c0;
}
*{box-sizing:border-box;margin:0;padding:0}
html,body{width:962px;height:1200px;overflow:hidden}
body{
  font-family:"Open Sans",Arial,sans-serif;
  color:var(--text);
  background:linear-gradient(160deg,var(--bg-top) 0%,#dcd2d3 50%,var(--bg-bottom) 100%);
  position:relative;
}
.screen-title{
  position:absolute;top:32px;left:0;width:962px;text-align:center;
  font-size:38px;font-weight:600;color:var(--title);letter-spacing:1px;
}
.app{
  position:absolute;left:158px;top:108px;width:645px;height:970px;
  background:#fff;box-shadow:0 2px 8px rgba(0,0,0,.12);
}
.topbar{position:absolute;left:0;top:0;width:100%;height:37px;background:var(--bar);color:#fff;font-size:10px}
.topbar .date{position:absolute;left:17px;top:12px;font-weight:600}
.radio{position:absolute;top:11px;color:#9aa0ab;font-size:10px;display:flex;align-items:center;gap:5px}
.radio i{width:9px;height:9px;border-radius:50%;background:#fff;display:block}
.radio.on i{border:2.5px solid #fff;background:var(--orange)}
.radio.teams{left:293px}
.radio.players{left:357px}
.search-input{position:absolute;left:419px;top:10px;width:146px;height:18px;background:#fff;border:1px solid #ccc;font-size:8px;color:#aaa;padding:3px 8px;font-style:italic}
.search-btn{position:absolute;left:569px;top:10px;width:62px;height:18px;background:var(--yellow);color:#333;font-size:10px;display:flex;align-items:center;justify-content:center;gap:4px}
.sidebar{position:absolute;left:0;top:37px;width:136px;bottom:16px;background:var(--side)}
.today-btn{position:absolute;left:15px;top:11px;width:99px;height:18px;background:var(--orange);color:#fff;font-size:7.5px;font-weight:700;display:flex;align-items:center;justify-content:center;gap:4px}
.side-head{position:absolute;left:0;width:136px;height:22px;background:var(--side-head);color:#e5e7eb;font-size:9px;padding:5px 0 0 14px}
.side-list{position:absolute;left:0;width:136px;list-style:none}
.side-list li{height:22.7px;border-bottom:1px solid var(--side-line);color:var(--side-text);font-size:9.5px;display:flex;align-items:center;padding-left:14px;gap:8px}
.side-list.plain li{padding-left:15px}
.flag{width:17px;height:11px;display:block;flex:none}
.more-btn{position:absolute;left:12px;width:52px;height:18px;background:var(--blue);color:#fff;font-size:9.5px;font-weight:600;display:flex;align-items:center;justify-content:center;gap:4px}
.content{position:absolute;left:136px;top:37px;width:509px;bottom:16px}
.profile{position:absolute;left:0;top:0;width:509px;height:66px;background:var(--profile);border-bottom:1px solid #e1e0da}
.avatar{position:absolute;left:18px;top:11px;width:45px;height:45px;border-radius:50%;background:radial-gradient(circle at 50% 45%,#8a6c5c,#3b2f2b 70%);border:3px solid #fff;box-shadow:0 0 0 1px #ddd}
.player-name{position:absolute;left:78px;top:17px;font-size:16px;font-weight:400;color:#2d2f36}
.player-team{position:absolute;left:78px;top:38px;font-size:9px;display:flex;align-items:center;gap:6px}
.shirt{position:absolute;right:18px;top:13px;width:37px;height:42px}
.pitch-box{position:absolute;left:17px;top:90px;width:215px;height:165px;border:1px solid #dcdcdc;padding:4px}
.pitch-fill{width:100%;height:100%;background:linear-gradient(180deg,var(--pitch-light),var(--pitch-mid))}
.info{position:absolute;left:250px;top:90px;width:242px;border-collapse:separate;border-spacing:0;font-size:9.5px}
.info td{height:24px;padding-left:11px}
.info tr:nth-child(odd){background:var(--row-b)}
.info tr:nth-child(even){background:var(--row-a)}
.info td.val{padding-left:0;width:134px;color:#222}
.panel{position:absolute;left:17px;width:474px;border:1px solid #e4e4e4;background:#fff}
.panel-head{height:24px;background:var(--bar);color:#fff;font-size:8.5px;font-weight:600;padding:6px 0 0 14px}
.season{top:280px;height:91px}
.grid-table{position:absolute;left:0;width:472px;font-size:9.5px}
.grid-table .row{position:relative;height:21.5px}
.grid-table .row span{position:absolute;top:50%;transform:translateY(-50%);white-space:nowrap}
.grid-table .row.head{font-size:8.5px;font-weight:700}
.grid-table .row.alt{background:var(--row-b)}
.c-center{width:20px;text-align:center;margin-left:-10px}
.career{top:392px;height:428px}
.chart{position:absolute;left:33px;top:47px;width:408px;height:144px}
.career-sep{position:absolute;left:0;top:210px;width:472px;border-top:1px solid var(--line)}
.team-cell{left:331px;display:flex;align-items:center;gap:6px}
.footer{position:absolute;left:0;bottom:0;width:100%;height:16px;background:var(--bar)}
</style>
</head>
<body>
<h1 class="screen-title">PLAYER SCREEN</h1>

<div class="app">
  <header class="topbar">
    <span class="date">25 September 2014</span>
    <span class="radio teams"><i></i>Teams</span>
    <span class="radio players on"><i></i>Players</span>
    <div class="search-input">Search</div>
    <div class="search-btn">
      <svg width="10" height="10" viewBox="0 0 10 10"><circle cx="4" cy="4" r="3" fill="none" stroke="#333" stroke-width="1.2"/><line x1="6.2" y1="6.2" x2="9.3" y2="9.3" stroke="#333" stroke-width="1.4"/></svg>
      Search
    </div>
  </header>

  <nav class="sidebar">
    <div class="today-btn">TODAY'S MATCHES
      <svg width="8" height="8" viewBox="0 0 8 8"><circle cx="4" cy="4" r="4" fill="#fff"/><path d="M3 2l2 2-2 2" fill="none" stroke="#e9592c" stroke-width="1.2"/></svg>
    </div>

    <div class="side-head" style="top:43px">DOMESTIC FOOTBALL</div>
    <ul class="side-list" style="top:65px">
      <li><svg class="flag" viewBox="0 0 17 11"><rect width="6" height="11" fill="#2a3fd0"/><rect x="6" width="5" height="11" fill="#fff"/><rect x="11" width="6" height="11" fill="#e8202a"/></svg>France</li>
      <li><svg class="flag" viewBox="0 0 17 11"><rect width="17" height="4" fill="#111"/><rect y="4" width="17" height="3.5" fill="#e8202a"/><rect y="7.5" width="17" height="3.5" fill="#f6c900"/></svg>Germany</li>
      <li><svg class="flag" viewBox="0 0 17 11"><rect width="6" height="11" fill="#1e9a3a"/><rect x="6" width="5" height="11" fill="#fff"/><rect x="11" width="6" height="11" fill="#e8202a"/></svg>Italy</li>
      <li><svg class="flag" viewBox="0 0 17 11"><rect width="17" height="11" fill="#2340b8"/><path d="M0 0L17 11M17 0L0 11" stroke="#fff" stroke-width="2"/></svg>Spain</li>
      <li><svg class="flag" viewBox="0 0 17 11"><rect width="17" height="11" fill="#e8202a"/><rect y="3" width="17" height="5" fill="#f6c900"/></svg>Scotland</li>
      <li><svg class="flag" viewBox="0 0 17 11"><rect width="17" height="11" fill="#fff"/><rect x="7" width="3" height="11" fill="#e8202a"/><rect y="4" width="17" height="3" fill="#e8202a"/></svg>England</li>
    </ul>
    <div class="more-btn" style="top:213px"><svg width="10" height="10" viewBox="0 0 10 10"><circle cx="5" cy="5" r="5" fill="#fff"/><path d="M5 2.5v5M2.5 5h5" stroke="#2f7fe0" stroke-width="1.4"/></svg>More</div>

    <div class="side-head" style="top:248px">CONTINENTAL FOOTBALL</div>
    <ul class="side-list plain" style="top:270px">
      <li>Elite Cup</li>
      <li>Elite Cup Qual.</li>
      <li>Continental Cup</li>
      <li>Continental Cup Qual.</li>
    </ul>
    <div class="more-btn" style="top:371px"><svg width="10" height="10" viewBox="0 0 10 10"><circle cx="5" cy="5" r="5" fill="#fff"/><path d="M5 2.5v5M2.5 5h5" stroke="#2f7fe0" stroke-width="1.4"/></svg>More</div>
  </nav>

  <main class="content">
    <section class="profile">
      <div class="avatar" role="img" aria-label="Player portrait photo"></div>
      <h2 class="player-name">Dario Vuković</h2>
      <div class="player-team"><svg class="flag" viewBox="0 0 17 11"><rect width="17" height="11" fill="#fff"/><rect x="7" width="3" height="11" fill="#e8202a"/><rect y="4" width="17" height="3" fill="#e8202a"/></svg>Westbridge FC</div>
      <svg class="shirt" viewBox="0 0 37 42" role="img" aria-label="Team shirt number 2">
        <path d="M10 2l5 2h7l5-2 9 6-3 9-5-2v26H9V15l-5 2-3-9z" fill="#2459c4"/>
        <text x="18.5" y="22" text-anchor="middle" font-family="Open Sans,Arial,sans-serif" font-size="13" font-weight="700" fill="#fff">2</text>
      </svg>
    </section>

    <div class="pitch-box">
      <div class="pitch-fill" role="img" aria-label="Pitch illustration showing the player's defensive position"></div>
    </div>

    <table class="info">
      <tr><td>Date of Birth</td><td class="val">22/02/1984</td></tr>
      <tr><td>Age</td><td class="val">30</td></tr>
      <tr><td>Place of Birth</td><td class="val">Sremska Mitrovica, Serbia</td></tr>
      <tr><td>Nationality</td><td class="val"><svg class="flag" style="display:inline-block;vertical-align:-2px;margin-right:3px" viewBox="0 0 17 11"><rect width="17" height="4" fill="#d0202a"/><rect y="4" width="17" height="3.5" fill="#2340b8"/><rect y="7.5" width="17" height="3.5" fill="#fff"/></svg>Serbia</td></tr>
      <tr><td>Height</td><td class="val">1.88 m / 6 ft&nbsp; 2 in</td></tr>
      <tr><td>Weight</td><td class="val">86 kg /13 st 8 lbs</td></tr>
      <tr><td>Position</td><td class="val">Defender</td></tr>
    </table>

    <section class="panel season">
      <div class="panel-head">THIS SEASON</div>
      <div class="grid-table" style="top:24px">
        <div class="row head">
          <span style="left:14px">COMPETITION</span>
          <span style="left:133px">TEAM</span>
          <span class="c-center" style="left:250px"><svg width="9" height="10" viewBox="0 0 9 10"><circle cx="4.5" cy="2" r="2" fill="#999"/><path d="M1 10V5.5Q1 4 2.5 4h4Q8 4 8 5.5V10z" fill="#999"/></svg></span>
          <span class="c-center" style="left:290px"><svg width="11" height="9" viewBox="0 0 11 9"><path d="M1 5l3 3 6-7" fill="none" stroke="#2fa52f" stroke-width="2"/></svg></span>
          <span class="c-center" style="left:330px"><svg width="10" height="10" viewBox="0 0 10 10"><path d="M2 1h6l-2 3" fill="none" stroke="#e8202a" stroke-width="1.6"/><path d="M8 9H2l2-3" fill="none" stroke="#2fa52f" stroke-width="1.6"/></svg></span>
          <span class="c-center" style="left:370px"><svg width="10" height="10" viewBox="0 0 10 10"><circle cx="5" cy="5" r="4.3" fill="#fff" stroke="#555"/><path d="M5 3.3l1.6 1.2-.6 1.9H4l-.6-1.9z" fill="#555"/></svg></span>
          <span class="c-center" style="left:410px"><svg width="8" height="10"><rect width="8" height="10" rx="1" fill="#f6e000"/></svg></span>
          <span class="c-center" style="left:450px"><svg width="8" height="10"><rect width="8" height="10" rx="1" fill="#e8202a"/></svg></span>
        </div>
        <div class="row alt">
          <span style="left:14px">Top Division</span><span style="left:133px">Westbridge FC</span>
          <span class="c-center" style="left:250px">5</span><span class="c-center" style="left:290px">5</span><span class="c-center" style="left:330px">-</span><span class="c-center" style="left:370px">2</span><span class="c-center" style="left:410px">1</span><span class="c-center" style="left:450px">-</span>
        </div>
        <div class="row">
          <span style="left:14px">Elite Cup</span><span style="left:133px">Westbridge FC</span>
          <span class="c-center" style="left:250px">1</span><span class="c-center" style="left:290px">1</span><span class="c-center" style="left:330px">-</span><span class="c-center" style="left:370px">-</span><span class="c-center" style="left:410px">-</span><span class="c-center" style="left:450px">-</span>
        </div>
      </div>
    </section>

    <section class="panel career">
      <div class="panel-head">CAREER</div>
      <svg class="chart" viewBox="430 730 510 180" role="img" aria-label="Career appearances and goals per season" font-family="Arial,sans-serif" font-size="8" fill="#222">
        <g stroke="#e3e3e3" stroke-width="1">
          <path d="M459 738.5H921M459 755.7H921M459 773H921M459 790.2H921M459 807.5H921M459 824.7H921M459 842H921M459 859.2H921"/>
          <path d="M486 738V876M513 738V876M540 738V876M568 738V876M595 738V876M622 738V876M650 738V876M677 738V876M705 738V876M732 738V876M759 738V876M786 738V876M813 738V876M840 738V876M868 738V876M895 738V876M921 738V876"/>
        </g>
        <polygon fill="#3166cf" points="459,780 513,787 540,876 568,876 596,822 650,780 705,760 759,776 813,760 868,752 921,860 921,876 459,876"/>
        <polygon fill="#f0132f" points="459,869 513,866 540,876 650,876 705,862 759,866 813,859 868,866 921,869 921,876 459,876"/>
        <path d="M459 738V876H921" fill="none" stroke="#888"/>
        <g text-anchor="end">
          <text x="453" y="741">40</text><text x="453" y="758">35</text><text x="453" y="776">30</text><text x="453" y="793">25</text><text x="453" y="810">20</text><text x="453" y="827">15</text><text x="453" y="845">10</text><text x="453" y="862">5</text>
        </g>
        <g text-anchor="middle">
          <text x="459" y="887">2006</text><text x="513" y="887">2007</text><text x="568" y="887">2008</text><text x="622" y="887">2009</text><text x="677" y="887">2010</text><text x="732" y="887">2011</text><text x="786" y="887">2012</text><text x="840" y="887">2013</text><text x="895" y="887">2014</text>
        </g>
        <rect x="637" y="895" width="7" height="7" fill="#3166cf"/><text x="648" y="901">Appearances</text>
        <rect x="712" y="895" width="7" height="7" fill="#f0132f"/><text x="723" y="901">Goals</text>
      </svg>
      <div class="career-sep"></div>
      <div class="grid-table" style="top:211px">
        <div class="row head">
          <span style="left:14px">SEASON</span>
          <span class="c-center" style="left:162px"><svg width="9" height="10" viewBox="0 0 9 10"><circle cx="4.5" cy="2" r="2" fill="#999"/><path d="M1 10V5.5Q1 4 2.5 4h4Q8 4 8 5.5V10z" fill="#999"/></svg></span>
          <span class="c-center" style="left:250px"><svg width="10" height="10" viewBox="0 0 10 10"><circle cx="5" cy="5" r="4.3" fill="#fff" stroke="#555"/><path d="M5 3.3l1.6 1.2-.6 1.9H4l-.6-1.9z" fill="#555"/></svg></span>
          <span style="left:331px">TEAM</span>
        </div>
        <div class="row alt"><span style="left:14px">2014 - 2015</span><span style="left:158px">5</span><span style="left:246px">2</span><span class="team-cell"><svg class="flag" viewBox="0 0 17 11"><rect width="17" height="11" fill="#fff"/><rect x="7" width="3" height="11" fill="#e8202a"/><rect y="4" width="17" height="3" fill="#e8202a"/></svg>Westbridge FC</span></div>
        <div class="row"><span style="left:14px">2013 - 2014</span><span style="left:158px">36</span><span style="left:246px">3</span><span class="team-cell"><svg class="flag" viewBox="0 0 17 11"><rect width="17" height="11" fill="#fff"/><rect x="7" width="3" height="11" fill="#e8202a"/><rect y="4" width="17" height="3" fill="#e8202a"/></svg>Westbridge FC</span></div>
        <div class="row alt"><span style="left:14px">2012 - 2013</span><span style="left:158px">34</span><span style="left:246px">5</span><span class="team-cell"><svg class="flag" viewBox="0 0 17 11"><rect width="17" height="11" fill="#fff"/><rect x="7" width="3" height="11" fill="#e8202a"/><rect y="4" width="17" height="3" fill="#e8202a"/></svg>Westbridge FC</span></div>
        <div class="row"><span style="left:14px">2011 - 2012</span><span style="left:158px">29</span><span style="left:246px">3</span><span class="team-cell"><svg class="flag" viewBox="0 0 17 11"><rect width="17" height="11" fill="#fff"/><rect x="7" width="3" height="11" fill="#e8202a"/><rect y="4" width="17" height="3" fill="#e8202a"/></svg>Westbridge FC</span></div>
        <div class="row alt"><span style="left:14px">2010 - 2011</span><span style="left:158px">34</span><span style="left:246px">4</span><span class="team-cell"><svg class="flag" viewBox="0 0 17 11"><rect width="17" height="11" fill="#fff"/><rect x="7" width="3" height="11" fill="#e8202a"/><rect y="4" width="17" height="3" fill="#e8202a"/></svg>Westbridge FC</span></div>
        <div class="row"><span style="left:14px">2009 - 2010</span><span style="left:158px">28</span><span style="left:246px">_</span><span class="team-cell"><svg class="flag" viewBox="0 0 17 11"><rect width="17" height="11" fill="#fff"/><rect x="7" width="3" height="11" fill="#e8202a"/><rect y="4" width="17" height="3" fill="#e8202a"/></svg>Westbridge FC</span></div>
        <div class="row alt"><span style="left:14px">2008 - 2009</span><span style="left:158px">16</span><span style="left:246px">_</span><span class="team-cell"><svg class="flag" viewBox="0 0 17 11"><rect width="17" height="11" fill="#fff"/><rect x="7" width="3" height="11" fill="#e8202a"/><rect y="4" width="17" height="3" fill="#e8202a"/></svg>Westbridge FC</span></div>
        <div class="row"><span style="left:14px">2007</span><span style="left:158px">26</span><span style="left:246px">3</span><span class="team-cell"><svg class="flag" viewBox="0 0 17 11"><rect width="17" height="4" fill="#fff"/><rect y="4" width="17" height="3.5" fill="#2340b8"/><rect y="7.5" width="17" height="3.5" fill="#e8202a"/></svg>Volga Rail</span></div>
        <div class="row alt"><span style="left:14px">2007</span><span style="left:158px">28</span><span style="left:246px">2</span><span class="team-cell"><svg class="flag" viewBox="0 0 17 11"><rect width="17" height="4" fill="#fff"/><rect y="4" width="17" height="3.5" fill="#2340b8"/><rect y="7.5" width="17" height="3.5" fill="#e8202a"/></svg>Volga Rail</span></div>
      </div>
    </section>
  </main>

  <footer class="footer"></footer>
</div>
</body>
</html>
```